Header für Blog zur Organisationsentwicklung
LunaKrie hat die Hinweise im Briefing und in den Kommentaren zu vorhandenen Designs gut aufgenommen und den Gestaltungsprozess vorangetrieben. So bekomme ich ein tolles Design, wo ich vorher keine Ahnung hatte, wie es aussehen sollte.
Zielgruppe
Ich bin freiberuflicher Organisationsberater und pflege auf meiner Website ein Blog zur Organisationsentwicklung. Dieses Blog soll zukünftig auf einer eigenen Domain erscheinen, sodass auch andere Kollegen sich daran beteiligen können. Daher soll mein Name nicht mehr im Vordergrund stehen - wenngleich ich immer noch als der Macher des Blog erkennbar bleiben soll.
Aufgabenstellung
Für das Blog "Labor für Unternehmenswandel" www.uw-labor.de wird ein ansprechender Header gesucht.
Der Header sollte den Namen des Blog und ein grafisches Element enthalten, dass der Bildsprache "Werkstatt", "Organisation", "Führung", etc. entnommen ist. Eventuell ein Element, das die Bildsprachen verbindet?
Da das Blog von einem Foto-Slider unter dem Header geprägt ist, sollte der Header nicht einfach aus einem Foto bestehen.
Die Farbgebung des Blog stellt die grafische Verbindung zu meiner Website www.hasselkamp.com her.
Mein Logo sollte im Header nicht verwendet werden, da ich das Blog bewusst von meiner Website löse, um weitere Beraterkollegen einzuladen, dabei mitzumachen

```html
<!DOCTYPE html>
<html lang="de">
<head>
<meta charset="utf-8">
<title>Labor für Unternehmenswandel – Blog-Header</title>
<link href="https://fonts.googleapis.com/css2?family=Source+Sans+3:wght@600&display=swap" rel="stylesheet">
<style>
  :root {
    --navy: #323267;
    --white: #ffffff;
  }
  html, body {
    margin: 0;
    padding: 0;
    overflow: hidden;
    background: var(--navy);
  }
  .blog-header {
    position: relative;
    width: 1200px;
    height: 102px;
    background: var(--navy);
    overflow: hidden;
  }
  .blog-title {
    position: absolute;
    left: 39px;
    top: 20px;
    margin: 0;
    font-family: "Source Sans 3", "Source Sans Pro", Arial, sans-serif;
    font-weight: 600;
    font-size: 38px;
    line-height: 46px;
    color: var(--white);
    letter-spacing: 0.2px;
  }
  .header-rule {
    position: absolute;
    left: 0;
    top: 86px;
    width: 1200px;
    height: 3px;
    background: var(--white);
  }
  .topic-icons {
    position: absolute;
    top: 18px;
    left: 918px;
    display: flex;
    gap: 0;
  }
  .topic-icon {
    position: absolute;
    fill: var(--white);
  }
  .icon-tool { left: 3px; top: 2px; }
  .icon-structure { left: 76px; top: 4px; }
  .icon-team { left: 162px; top: 0; }
</style>
</head>
<body>
<header class="blog-header">
  <h1 class="blog-title">Labor für Unternehmenswandel</h1>

  <div class="topic-icons" aria-hidden="true">
    <svg class="topic-icon icon-tool" width="52" height="50" viewBox="0 0 52 50">
      <g transform="rotate(-45 26 25)">
        <rect x="4" y="21" width="34" height="9" rx="4.5"/>
        <path d="M36 13 a13 13 0 1 0 0 25 l0 -7 l7 0 l0 -11 l-7 0 z"/>
      </g>
    </svg>

    <svg class="topic-icon icon-structure" width="50" height="46" viewBox="0 0 50 46">
      <rect x="17" y="0" width="16" height="13" rx="2"/>
      <rect x="23.5" y="13" width="3" height="8"/>
      <rect x="6" y="20" width="38" height="3"/>
      <rect x="6" y="20" width="3" height="11"/>
      <rect x="23.5" y="20" width="3" height="11"/>
      <rect x="41" y="20" width="3" height="11"/>
      <rect x="0" y="31" width="15" height="14" rx="2"/>
      <rect x="17.5" y="31" width="15" height="14" rx="2"/>
      <rect x="35" y="31" width="15" height="14" rx="2"/>
    </svg>

    <svg class="topic-icon icon-team" width="60" height="50" viewBox="0 0 60 50">
      <circle cx="11" cy="13" r="7"/>
      <path d="M0 38 q0 -15 11 -15 q6 0 9 4 q-5 5 -5 11 z"/>
      <circle cx="49" cy="13" r="7"/>
      <path d="M60 38 q0 -15 -11 -15 q-6 0 -9 4 q5 5 5 11 z"/>
      <circle cx="30" cy="11" r="10"/>
      <path d="M13 48 q0 -23 17 -23 q17 0 17 23 z"/>
    </svg>
  </div>

  <div class="header-rule"></div>
</header>
</body>
</html>
```